Business Card Design

We are a florist shop that also stocks a range of giftware and jewellery. I would like a new design that incorporates a light green background. If you could use a skeleton leaf somewhere in the design that would be great. I would also like to incorporate the find us on Friendlink logo on this design.

Industry/Entity Type

Florist

Contact Information for Business Card

Petals on Larkmore
41 Brindle street
Elmvale Victoria 3871
Phone: 0352983047
Fax : 0352983066
email: pol@wrenmail.net.au

Proprietors : Dana & Lee Thornwick

```html
<!DOCTYPE html>
<html lang="en">
<head>
<meta charset="utf-8">
<title>Petals on Larkmore – Business Card</title>
<link href="https://fonts.googleapis.com/css2?family=Fanwood+Text&display=swap" rel="stylesheet">
<style>
  :root {
    --page: #ffffff;
    --frame: #1a1a1a;
    --card-pale: #eef1df;
    --card-mid: #c9d49a;
    --card-deep: #a8b85a;
    --band: #d4dbaf;
    --ink: #ffffff;
    --badge: #6f7a3c;
  }
  html, body {
    margin: 0;
    width: 1200px;
    height: 822px;
    overflow: hidden;
    background: var(--page);
  }
  .canvas {
    position: relative;
    width: 1200px;
    height: 822px;
    box-sizing: border-box;
    border: 2px solid var(--frame);
    background: var(--page);
  }
  .card {
    position: absolute;
    left: 186px;
    top: 164px;
    width: 839px;
    height: 507px;
    overflow: hidden;
    background: linear-gradient(90deg, var(--card-pale) 0%, #dfe5c2 30%, var(--card-mid) 65%, var(--card-deep) 100%);
  }
  .card__shapes {
    position: absolute;
    inset: 0;
  }
  .card__floral {
    position: absolute;
    left: 0;
    top: 0;
    width: 262px;
    height: 507px;
  }
  .contact {
    position: absolute;
    left: 290px;
    top: 246px;
    margin: 0;
    font-family: "Fanwood Text", Georgia, serif;
    font-size: 31px;
    line-height: 43px;
    letter-spacing: 1.4px;
    color: var(--ink);
    font-style: normal;
  }
  .contact__line { display: block; white-space: nowrap; }
  .social {
    position: absolute;
    right: 38px;
    bottom: 12px;
    display: flex;
    align-items: center;
    gap: 9px;
    font-family: "Fanwood Text", Georgia, serif;
    font-size: 23px;
    letter-spacing: 0.8px;
    color: var(--ink);
    white-space: nowrap;
  }
  .social__mark {
    width: 24px;
    height: 24px;
    background: var(--badge);
  }
</style>
</head>
<body>
  <main class="canvas">
    <section class="card" aria-label="Business card">
      <svg class="card__shapes" viewBox="0 0 839 507" width="839" height="507" aria-hidden="true">
        <defs>
          <linearGradient id="swoop" x1="0" y1="0" x2="1" y2="0">
            <stop offset="0" stop-color="#f2f4e6"/>
            <stop offset="0.5" stop-color="#e2e8c6" stop-opacity="0.6"/>
            <stop offset="1" stop-color="#d4dbaf" stop-opacity="0"/>
          </linearGradient>
        </defs>
        <path d="M0,20 C200,170 480,225 839,205 L839,230 C480,250 200,200 0,60 Z" fill="url(#swoop)"/>
        <path d="M0,0 L839,0 L839,207 C560,228 250,175 0,18 Z" fill="var(--band)"/>
      </svg>
      <svg class="card__floral" viewBox="0 0 262 507" width="262" height="507" role="img" aria-label="White floral vine ornament with leaves and blossoms">
        <defs>
          <linearGradient id="floralTone" x1="0" y1="0" x2="1" y2="0">
            <stop offset="0" stop-color="#ffffff" stop-opacity="0.6"/>
            <stop offset="1" stop-color="#ffffff" stop-opacity="0"/>
          </linearGradient>
        </defs>
        <rect x="0" y="0" width="262" height="507" fill="url(#floralTone)"/>
      </svg>
      <address class="contact">
        <span class="contact__line">Petals on Larkmore 41,</span>
        <span class="contact__line">Brindle street Elmvale Victoria 3871</span>
        <span class="contact__line">Phone: 0352983047 Fax : 0352983066</span>
        <span class="contact__line">email: pol@wrenmail.net.au</span>
        <span class="contact__line">Proprietors : Dana &amp; Lee Thornwick</span>
      </address>
      <div class="social">
        <span>Find us on Friendlink</span>
        <span class="social__mark" aria-hidden="true"></span>
      </div>
    </section>
  </main>
</body>
</html>
```